Need 8 icons (technology and data)

We are a start up working with cutting edge technology and data, specifically the following technologies:
- text analytics (also called "natural language processing")
- machine learning (also called "artificial intelligence")
- robotics
- real-time data processing

and the following data sources:
- social media conversation
- crowdsourced information
- sensor data
- interest graph data (also called "social interests data")

These 8 topics should be represented by icons that should be easy to recognize with or without description text next to the icon.

There are some existing common visuals for some of these topics, e.g. speech bubble for social media conversation.

Target Market(s)

Software engineers, web developers, IT managers

Industry/Entity Type

Learning

Requirements
Must have
• - the 8 icons should be consistent in style.
- text describing the icon will be placed to the right
- the 8 icons must be provided in vector format and PNG format (transparent background).
Nice to have
• - it would be nice if the icons were spherical Tarvix style icons or have an Zeb icon look and feel.

Other information:

- please look at the home page mockup in the PDF... it shows how the icons are animated and appear to "rain down" behind the central blue ribbon.

- the font used on the home page is the Vorplex Web font called "Oswald".
Should not have
• - Colors that clash with the current color palette of the home page (blue / grey / green / white / black).

- brain metaphor / visual for artificial intelligence / machine learning icon.

```html
<!DOCTYPE html>
<html lang="en">
<head>
<meta charset="utf-8">
<title>Technology and Data Icons</title>
<link rel="stylesheet" href="https://fonts.googleapis.com/css2?family=Oswald:wght@400;500&display=swap">
<style>
  :root {
    --bg: #ffffff;
    --ink: #000000;
    --green: #4fae3c;
    --green-light: #7fd064;
    --green-dark: #2f7a22;
    --glyph: #3a3a3a;
    --glyph-light: #9a9a9a;
  }
  * { margin: 0; padding: 0; box-sizing: border-box; }
  html, body { width: 1200px; height: 592px; overflow: hidden; background: var(--bg); }
  .board {
    position: relative; width: 1200px; height: 592px;
    font-family: "Oswald", sans-serif; color: var(--ink);
    font-size: 14px; font-weight: 500; letter-spacing: -0.3px;
  }
  .art { position: absolute; }
  .art-operator {
    left: 0; top: 0; width: 123px; height: 140px;
    background: radial-gradient(circle at 40% 40%, #5a5a5a, #111 75%);
    border-radius: 0 0 60px 0;
  }
  .art-team {
    left: 162px; top: 205px; width: 72px; height: 67px;
    background: radial-gradient(circle at 50% 45%, #6a6a6a, #1a1a1a 80%);
    border-radius: 30px;
  }
  .note { position: absolute; white-space: nowrap; line-height: 1; }
  .note-nlp { left: 393px; top: 104px; }
  .note-ai { left: 127px; top: 341px; }
  .note-interests { left: 860px; top: 374px; }
  .topic { position: absolute; display: flex; align-items: center; }
  .topic-icon { width: 68px; height: 68px; flex: none; }
  .topic-label { white-space: nowrap; line-height: 1; }
  .col-tech .topic-label { margin-left: 14px; }
  .col-data .topic-label { margin-left: 20px; }
</style>
</head>
<body>
<div class="board">
  <div class="art art-operator" role="img" aria-label="Line drawing of a support operator in profile wearing a headset"></div>
  <p class="note note-nlp">(also called "natural language processing")</p>

  <div class="art art-team" role="img" aria-label="Line drawing of three heads grouped together"></div>
  <p class="note note-ai">- (also called "artificial intelligence")</p>

  <p class="note note-interests">(also called "social interests data")</p>

  <svg width="0" height="0" style="position:absolute">
    <defs>
      <radialGradient id="orb" cx="40%" cy="35%" r="70%">
        <stop offset="0" stop-color="#7fd064"/>
        <stop offset="0.6" stop-color="#4fae3c"/>
        <stop offset="1" stop-color="#2f7a22"/>
      </radialGradient>
    </defs>
  </svg>

  <div class="topic col-tech" style="left:369px; top:218px;">
    <svg class="topic-icon" viewBox="0 0 68 68" role="img" aria-label="Text analytics icon">
      <circle cx="34" cy="34" r="32" fill="url(#orb)" stroke="var(--green-dark)" stroke-width="2"/>
      <text x="34" y="40" text-anchor="middle" font-family="Oswald, sans-serif" font-size="17" font-weight="500" fill="var(--glyph-light)">a[bc]d</text>
    </svg>
    <span class="topic-label">-text analytics</span>
  </div>

  <div class="topic col-tech" style="left:369px; top:318px;">
    <svg class="topic-icon" viewBox="0 0 68 68" role="img" aria-label="Machine learning icon: a laptop">
      <circle cx="34" cy="34" r="32" fill="url(#orb)" stroke="var(--green-dark)" stroke-width="2"/>
      <rect x="18" y="16" width="30" height="22" rx="2" fill="var(--glyph-light)" stroke="var(--glyph)" stroke-width="2"/>
      <path d="M12 46 L48 46 L56 38 L22 38 Z" fill="var(--glyph)"/>
    </svg>
    <span class="topic-label">-machine learning</span>
  </div>

  <div class="topic col-tech" style="left:369px; top:420px;">
    <svg class="topic-icon" viewBox="0 0 68 68" role="img" aria-label="Social media conversation icon: a speech bubble">
      <circle cx="34" cy="34" r="32" fill="url(#orb)" stroke="var(--green-dark)" stroke-width="2"/>
      <path d="M14 22 Q14 18 18 18 H50 Q54 18 54 22 V38 Q54 42 50 42 H24 L14 50 L18 42 Q14 42 14 38 Z" fill="var(--glyph-light)" stroke="var(--glyph)" stroke-width="2"/>
    </svg>
    <span class="topic-label">- social media conversation</span>
  </div>

  <div class="topic col-tech" style="left:369px; top:523px;">
    <svg class="topic-icon" viewBox="0 0 68 68" role="img" aria-label="Sensor data icon: a sensor probe">
      <circle cx="34" cy="34" r="32" fill="url(#orb)" stroke="var(--green-dark)" stroke-width="2"/>
      <path d="M21 17 L24 33 L47 49" fill="none" stroke="var(--glyph)" stroke-width="3" stroke-linecap="round" stroke-linejoin="round"/>
    </svg>
    <span class="topic-label">- sensor data</span>
  </div>

  <div class="topic col-data" style="left:602px; top:218px;">
    <svg class="topic-icon" viewBox="0 0 68 68" role="img" aria-label="Robotics icon: a robot figure">
      <circle cx="34" cy="34" r="32" fill="url(#orb)" stroke="var(--green-dark)" stroke-width="2"/>
      <circle cx="34" cy="34" r="18" fill="var(--glyph-light)" opacity="0.8"/>
    </svg>
    <span class="topic-label">- robotics</span>
  </div>

  <div class="topic col-data" style="left:602px; top:318px;">
    <svg class="topic-icon" viewBox="0 0 68 68" role="img" aria-label="Interest graph data icon: a bar chart">
      <circle cx="34" cy="34" r="32" fill="url(#orb)" stroke="var(--green-dark)" stroke-width="2"/>
      <circle cx="34" cy="34" r="20" fill="#fff" stroke="var(--ink)" stroke-width="2"/>
      <g fill="var(--ink)">
        <rect x="22" y="36" width="4" height="16"/>
        <rect x="28" y="28" width="4" height="24"/>
        <rect x="34" y="22" width="4" height="30"/>
        <rect x="40" y="30" width="4" height="22"/>
        <rect x="46" y="38" width="3" height="12"/>
      </g>
    </svg>
    <span class="topic-label">- interest graph data</span>
  </div>

  <div class="topic col-data" style="left:602px; top:420px;">
    <svg class="topic-icon" viewBox="0 0 68 68" role="img" aria-label="Real-time data processing icon: a clock">
      <circle cx="34" cy="34" r="32" fill="url(#orb)" stroke="var(--green-dark)" stroke-width="2"/>
      <circle cx="34" cy="34" r="22" fill="#fff" stroke="var(--ink)" stroke-width="2.5"/>
      <g stroke="var(--ink)" stroke-width="1.5">
        <line x1="34" y1="14" x2="34" y2="18"/><line x1="34" y1="50" x2="34" y2="54"/>
        <line x1="14" y1="34" x2="18" y2="34"/><line x1="50" y1="34" x2="54" y2="34"/>
      </g>
      <path d="M34 34 L34 20 M34 34 L44 40" stroke="var(--ink)" stroke-width="2" fill="none"/>
    </svg>
    <span class="topic-label">- real-time data processing</span>
  </div>

  <div class="topic col-data" style="left:602px; top:523px;">
    <svg class="topic-icon" viewBox="0 0 68 68" role="img" aria-label="Crowdsourced information icon: a group of people">
      <circle cx="34" cy="34" r="32" fill="url(#orb)" stroke="var(--green-dark)" stroke-width="2"/>
      <circle cx="34" cy="36" r="18" fill="var(--glyph)" opacity="0.55"/>
    </svg>
    <span class="topic-label">- crowdsourced information</span>
  </div>
</div>
</body>
</html>
```